Drowsy Heron

Need a business card for our restaurant. Restaurant and Bar in the mountains of North Idaho. Rustic looking card

Contact Information for Business Card

rustic design, wood and metal looking, primarily neutral colors

Requirements
Must have
• Name, address, phone number, website, email address

```html
<!DOCTYPE html>
<html lang="en">
<head>
<meta charset="UTF-8">
<title>Drowsy Heron – Business Card</title>
<link href="https://fonts.googleapis.com/css2?family=Montserrat:wght@400;700&display=swap" rel="stylesheet">
<style>
  :root {
    --backdrop: #2b2b2b;
    --card: #1b1b1b;
    --card-edge: #262626;
    --ink: #f4f4f4;
    --ink-soft: #d6d6d6;
    --mark-faint: #2a2a2a;
  }
  html, body {
    margin: 0;
    padding: 0;
    width: 1200px;
    height: 875px;
    overflow: hidden;
    background: var(--backdrop);
    font-family: "Montserrat", sans-serif;
  }
  .canvas {
    position: relative;
    width: 1200px;
    height: 875px;
  }
  .card {
    position: absolute;
    width: 540px;
    height: 310px;
    background: var(--card);
    border-radius: 18px;
    border: 1px solid var(--card-edge);
    box-shadow: 0 20px 50px rgba(0,0,0,0.55);
    overflow: hidden;
  }
  .card--front { left: 90px; top: 100px; }
  .card--back { left: 570px; top: 465px; }

  .brand {
    display: flex;
    align-items: center;
    gap: 14px;
    color: var(--ink);
    font-weight: 700;
  }
  .brand__dot {
    width: 18px;
    height: 18px;
    border-radius: 50%;
    background: var(--ink);
    flex: none;
  }
  .card--front .brand {
    position: absolute;
    left: 50%;
    top: 50%;
    transform: translate(-50%, -50%);
    font-size: 34px;
    white-space: nowrap;
  }
  .card--back .brand {
    position: absolute;
    left: 34px;
    top: 36px;
    font-size: 20px;
  }
  .card--back .brand__dot { width: 12px; height: 12px; }

  .brand-watermark {
    position: absolute;
    right: 34px;
    top: 60px;
    font-size: 40px;
    font-weight: 700;
    line-height: 1.05;
    color: var(--mark-faint);
    text-align: right;
  }

  .contact {
    position: absolute;
    left: 34px;
    bottom: 30px;
    color: var(--ink-soft);
    font-size: 13px;
    line-height: 1.35;
  }
  .contact__name {
    margin: 0;
    color: var(--ink);
    font-size: 22px;
    font-weight: 700;
  }
  .contact__role { margin: 0 0 12px; }
  .contact__address { margin: 0 0 12px; font-style: normal; }
  .contact__list { list-style: none; margin: 0; padding: 0; }
  .contact__list li {
    display: flex;
    align-items: center;
    gap: 10px;
    margin-bottom: 3px;
  }
  .contact__list svg { width: 13px; height: 13px; fill: var(--ink); flex: none; }
</style>
</head>
<body>
<main class="canvas">
  <section class="card card--front">
    <div class="brand"><span class="brand__dot"></span>Drowsy Heron</div>
  </section>

  <section class="card card--back">
    <div class="brand"><span class="brand__dot"></span>Drowsy Heron</div>
    <div class="brand-watermark" aria-hidden="true">Drowsy<br>Heron</div>
    <div class="contact">
      <p class="contact__name">Evan Marlow</p>
      <p class="contact__role">Managing Director</p>
      <address class="contact__address">48 Cedar Ridge Road,<br>Pinecrest, USA</address>
      <ul class="contact__list">
        <li>
          <svg viewBox="0 0 24 24" aria-hidden="true"><path d="M6.6 10.8a15.1 15.1 0 0 0 6.6 6.6l2.2-2.2a1 1 0 0 1 1-.25 11.4 11.4 0 0 0 3.6.57 1 1 0 0 1 1 1V20a1 1 0 0 1-1 1A17 17 0 0 1 3 4a1 1 0 0 1 1-1h3.5a1 1 0 0 1 1 1c0 1.25.2 2.45.57 3.57a1 1 0 0 1-.25 1z"/></svg>
          (08) 4410 2286
        </li>
        <li>
          <svg viewBox="0 0 24 24" aria-hidden="true"><path d="M2 5h20v14H2zm2 2v.5l8 5 8-5V7l-8 5z"/></svg>
          hello@drowsyheron.com
        </li>
        <li>
          <svg viewBox="0 0 24 24" aria-hidden="true"><path d="M12 2a10 10 0 1 0 0 20 10 10 0 0 0 0-20zm0 2c.9 0 2.2 1.9 2.8 5H9.2C9.8 5.9 11.1 4 12 4zM4.3 11h2.8a17 17 0 0 0 0 2H4.3a8 8 0 0 1 0-2zm4.9 0h5.6a15 15 0 0 1 0 2H9.2a15 15 0 0 1 0-2zm7.7 0h2.8a8 8 0 0 1 0 2h-2.8a17 17 0 0 0 0-2zM9.2 15h5.6c-.6 3.1-1.9 5-2.8 5s-2.2-1.9-2.8-5z"/></svg>
          www.drowsyheron.com
        </li>
      </ul>
    </div>
  </section>
</main>
</body>
</html>
```